Brivora Distance Learning Website

Brivora provide e-learning and mixed learning solutions for individuals, colleges, organisations and B2B.
We need a modern, light and flat website design for Brivora. We want to to see the designer incorporate user experience(UX) design elements into the AI or PSD mockups. We would like to see designs that use pastel colors that compliment yellow and black of our logo.
We want our E-learning experience to accelerate learning and for the interface to be user friendly and intuitive. We want the designs to focus on quick access to course information, course reviews, learning progress and study advice. Quick and intuitive access to all content for our clients is one of our top priorities.
We would like designs for the following project 3 pages:
1. Learner homepage dashboard (see attached screenshot).
On this page the Learners need to:
- Login
- Have quick access to Packages and Courses.
- See other recommended courses (Below Packages and Courses)
- Possibly a left hand side column/menu with thumbnail icons (See lumivex learner dashboard screenshot)
2. Homepage
See current sample
http://www.brivora-learn.test
We would like the designer to focus on creating a customized banner to enhance the home page.
3. Primary Landing/Marketing page
This page is geared towards customer acquisition with the focal point being the top banner (video or HD image).
And Course Preview content below.
See reference
http://brivora-learn.test/subscriptionPlans/marketing/MTc%3D/Mjc4Nw%3D%3D/Quick%20Fennish%20%2B%20Fennish%20Nibbles%20Bundle%20by%20Harold%20Wen%20Pike
Other site we like:
- https://www.korvanta.test (We like the home page and top bar on courses page)
- http://www.tutorglen.test
- http://crewmapleden.test (think this site looks great, love the lower graphics on the homepage)
Updates
Hello,
Thank you for taking the time to contribute to this web design competition. We would just like to point out a few things:
1. Please try to make the color palette similar to the colors used in the screenshot that we just uploaded ('possible color palette).
2. Please make the designs specific to each page: THE LEARNER HOMEPAGE, HOME PAGE, and the MARKETING LANDING PAGE.
We are very happy with the high quality of designs so far,
Cheers,
Lee Ab
KV-Studio
Also,
Please avoid using dark/bold elements in the designs. The ONLY elements that we want to be dark are the logo and the footer.
Any questions please ask,
Cheers,
Lee Ab
Kv-Studio
Hello,
Based on the round of feedback we just gave it would be great if you could complete further design changes by tomorrow, as we are pushed for time.
Thank you,
Lee Ab
KV-Studio

```html
<!DOCTYPE html>
<html lang="en">
<head>
<meta charset="utf-8">
<title>Brivora — Distance Learning</title>
<link href="https://fonts.googleapis.com/css2?family=Open+Sans:ital,wght@0,400;0,600;0,700;0,800;1,400&display=swap" rel="stylesheet">
<style>
:root{
  --yellow:#f5c518;
  --yellow-dark:#d9a400;
  --ink:#222222;
  --text:#333333;
  --muted:#777777;
  --grey-bg:#e3e3e3;
  --light:#f4f4f4;
  --band:#e9e7e2;
  --band-line:#d3d0c8;
  --footer:#1e1e1e;
  --white:#ffffff;
  --star:#f0a500;
}
*{box-sizing:border-box;margin:0;padding:0}
html,body{width:1200px;height:2724px;overflow:hidden}
body{font-family:"Open Sans",Arial,sans-serif;color:var(--text);background:var(--white)}
a{color:inherit;text-decoration:none}

/* Hero */
.hero{position:relative;height:820px;overflow:hidden}
.hero-photo{position:absolute;inset:0;background:linear-gradient(160deg,#d9c7ab 0%,#c8b092 40%,#b89e80 75%,#a98f72 100%)}
.hero-shade{position:absolute;inset:0;background:rgba(60,45,30,.12)}
.site-header{position:absolute;top:0;left:0;right:0;height:96px;display:flex;align-items:center;padding:0 120px;background:rgba(255,255,255,.18)}
.brand{display:flex;align-items:center;gap:12px;color:var(--ink);font-weight:800;font-size:40px;letter-spacing:-.5px}
.brand-dot{width:42px;height:42px;border-radius:50%;background:var(--yellow)}
.main-nav{margin-left:auto;display:flex;gap:8px;align-items:center}
.main-nav a{color:var(--white);font-weight:700;font-size:17px;padding:10px 14px;text-shadow:0 1px 3px rgba(0,0,0,.45)}
.main-nav a.active{background:var(--yellow);color:var(--ink);text-shadow:none}
.nav-login{margin-left:24px;display:flex;align-items:center;gap:8px;color:var(--white);font-size:17px;font-weight:600;text-shadow:0 1px 3px rgba(0,0,0,.45)}
.nav-login i{width:30px;height:30px;background:var(--white);display:block}
.hero-copy{position:absolute;top:290px;left:0;right:0;text-align:center;color:var(--white);font-size:40px;font-weight:700;line-height:1.3;text-shadow:0 2px 8px rgba(0,0,0,.55)}
.hero-copy em{font-style:normal;color:var(--yellow)}
.hero-search{position:absolute;top:490px;left:320px;width:560px;height:64px;display:flex}
.hero-search span{flex:1;background:var(--white);font-size:26px;color:#aaa;padding:14px 22px}
.hero-search b{width:72px;background:var(--yellow);display:flex;align-items:center;justify-content:center}
.hero-link{position:absolute;top:580px;left:0;right:0;text-align:center;color:var(--white);font-size:22px;font-weight:700;text-decoration:underline;text-shadow:0 1px 4px rgba(0,0,0,.5)}

/* Features */
.features{height:320px;background:var(--grey-bg);display:flex;justify-content:center;gap:60px;padding-top:52px}
.feature{width:230px;text-align:center}
.feature-icon{width:116px;height:116px;margin:0 auto 16px;border-radius:50%;background:var(--white);display:flex;align-items:center;justify-content:center}
.feature h3{font-size:20px;font-weight:700;color:var(--ink);margin-bottom:8px}
.feature p{font-size:13px;line-height:1.45;color:#555}

/* Courses */
.courses{height:520px;background:var(--light);position:relative;padding-top:42px}
.section-title{text-align:center;font-size:34px;font-weight:800;color:var(--ink)}
.section-title span{color:var(--yellow)}
.carousel-arrows{position:absolute;top:96px;right:124px;display:flex;gap:6px}
.carousel-arrows i{width:24px;height:24px;border:2px solid #555;background:var(--white);display:block}
.course-grid{display:flex;justify-content:center;gap:18px;margin-top:38px}
.course-card{width:228px;height:290px;background:var(--white);box-shadow:0 1px 4px rgba(0,0,0,.15)}
.course-thumb{height:128px}
.course-card h4{font-size:14px;font-weight:600;text-align:center;padding:10px 8px 6px;line-height:1.3;height:54px}
.course-meta{display:flex;justify-content:space-between;align-items:center;padding:4px 10px;font-size:12px;color:var(--muted)}
.stars{color:var(--star);font-size:15px;letter-spacing:1px}
.price{font-size:20px;font-weight:700;color:var(--ink)}
.course-tutor{display:flex;align-items:center;gap:8px;border-top:1px solid #e4e4e4;margin:8px 10px 0;padding-top:8px}
.course-tutor .avatar{width:34px;height:34px;background:#b8a48e}
.course-tutor b{font-size:13px;display:block}
.course-tutor small{font-size:11px;color:var(--muted)}
.more-btn{display:block;width:170px;margin:34px auto 0;border:2px solid #555;background:var(--white);text-align:center;font-size:14px;font-weight:600;padding:10px 0}

/* Band */
.info-band{height:460px;background:var(--band);display:flex;justify-content:center;gap:48px;padding-top:34px}
.band-col{width:300px}
.band-col h3{font-size:22px;color:var(--ink);font-weight:700;margin-bottom:16px}
.band-col h3 span{color:var(--yellow-dark)}
.news-list{background:var(--white);padding:10px;border:1px solid var(--band-line)}
.news-item{display:flex;gap:10px;padding:8px 0;border-bottom:1px solid #e6e6e6}
.news-item:last-child{border-bottom:none}
.news-item i{width:60px;height:56px;background:var(--yellow);display:block;flex:none}
.news-item b{font-size:13px;display:block;line-height:1.3}
.news-item small{font-size:12px;color:var(--muted)}
.join-form .field{background:var(--white);border:1px solid var(--band-line);height:42px;margin-bottom:10px;font-size:14px;color:#999;padding:10px 12px}
.join-form .field.tall{height:104px}
.join-form .join-btn{display:block;margin-left:auto;width:90px;background:var(--yellow);color:var(--ink);font-weight:800;font-size:20px;text-align:center;padding:8px 0}
.join-form p{color:#555;font-size:12px;line-height:1.4;margin-top:14px;text-align:center}
.tutor-card{background:var(--white);border:1px solid var(--band-line);padding:22px;text-align:center}
.tutor-photo{width:124px;height:124px;border-radius:50%;margin:0 auto 12px;background:linear-gradient(135deg,#b9a591,#8a776a)}
.tutor-card h4{font-size:20px;color:var(--yellow-dark);font-weight:700}
.tutor-card .role{font-size:14px;font-weight:600;margin:2px 0 8px}
.tutor-card p{font-size:12px;line-height:1.45;color:#666}
.tutor-card .profile-btn{display:inline-block;margin-top:14px;background:var(--yellow);font-weight:700;font-size:13px;padding:9px 18px;color:var(--ink)}

/* Testimonials */
.testimonials{height:400px;background:var(--white);text-align:center;padding-top:44px}
.testimonials blockquote{width:820px;margin:22px auto 0;font-style:italic;font-size:17px;line-height:1.5;color:#555}
.student-photo{width:132px;height:132px;border-radius:50%;margin:22px auto 8px;border:5px solid var(--yellow);background:linear-gradient(135deg,#dcc0a4,#b09078)}
.student-name{font-size:14px;font-weight:700;color:var(--yellow-dark);letter-spacing:1px}
.dots{display:flex;gap:10px;justify-content:center;margin-top:22px}
.dots i{width:16px;height:16px;border-radius:50%;background:#ccc;display:block}
.dots i.on{background:#888}

/* Footer */
.site-footer{height:204px;background:var(--footer);color:#ccc;text-align:center;padding-top:26px}
.social{display:flex;justify-content:center;gap:24px}
.social-box{display:flex;align-items:center;gap:10px;color:var(--white)}
.social-box i{width:44px;height:44px;background:var(--yellow);display:block}
.social-box b{font-size:15px;display:block;text-align:left}
.social-box small{font-size:13px;display:block;text-align:left}
.footer-nav{display:flex;justify-content:center;gap:22px;margin-top:40px;font-size:14px;font-weight:600;color:var(--white)}
.copyright{font-size:13px;margin-top:14px;color:#aaa}
</style>
</head>
<body>

<section class="hero">
  <div class="hero-photo" role="img" aria-label="Photo from above of students working on laptops at a light wooden table"></div>
  <div class="hero-shade"></div>
  <header class="site-header">
    <div class="brand"><span class="brand-dot"></span>Brivora</div>
    <nav class="main-nav">
      <a class="active" href="#">HOME</a>
      <a href="#">COURSES</a>
      <a href="#">ABOUT</a>
      <a href="#">CONTACT</a>
      <span class="nav-login"><i></i>Login | Register</span>
    </nav>
  </header>
  <h1 class="hero-copy">Facilitating Elegant <em>E-LEARNING</em> &amp; Mixed Learning<br>Solutions For <em>INDIVIDUALS</em>, Colleges, Organisations<br>&amp; B2B.</h1>
  <div class="hero-search">
    <span>Search ...</span>
    <b><svg width="30" height="30" viewBox="0 0 24 24"><circle cx="10" cy="10" r="6.5" fill="none" stroke="#fff" stroke-width="2.6"/><line x1="15" y1="15" x2="21" y2="21" stroke="#fff" stroke-width="2.8" stroke-linecap="round"/></svg></b>
  </div>
  <a class="hero-link" href="#">View All Courses &gt;&gt;</a>
</section>

<section class="features">
  <div class="feature">
    <div class="feature-icon"><svg width="56" height="56" viewBox="0 0 24 24"><path d="M2 10h4v11H2zM8 21V10l5-8c1.5 0 2.5 1 2 3l-1 4h6c1.2 0 2 1 1.8 2.2l-1.6 8A2 2 0 0 1 18.2 21z" fill="#f5c518"/></svg></div>
    <h3>Great Material</h3>
    <p>Lorem ipsum dolor sit amet, consectetur adipiscing elit, sed do eiusmod tempor incididunt.</p>
  </div>
  <div class="feature">
    <div class="feature-icon"><svg width="56" height="56" viewBox="0 0 24 24"><circle cx="9" cy="9" r="5" fill="none" stroke="#f5c518" stroke-width="3"/><circle cx="17" cy="16" r="4" fill="none" stroke="#f5c518" stroke-width="3"/></svg></div>
    <h3>High Quality</h3>
    <p>Lorem ipsum dolor sit amet, consectetur adipiscing elit, sed do eiusmod tempor incididunt.</p>
  </div>
  <div class="feature">
    <div class="feature-icon"><svg width="56" height="56" viewBox="0 0 24 24"><path d="M12 21 3.5 12.5A5 5 0 0 1 12 5.5a5 5 0 0 1 8.5 7z" fill="#f5c518"/></svg></div>
    <h3>Learning Is Fun</h3>
    <p>Lorem ipsum dolor sit amet, consectetur adipiscing elit, sed do eiusmod tempor incididunt.</p>
  </div>
  <div class="feature">
    <div class="feature-icon"><svg width="56" height="56" viewBox="0 0 24 24"><path d="M4 12.5 9.5 18 20 6" fill="none" stroke="#f5c518" stroke-width="3.5" stroke-linecap="round" stroke-linejoin="round"/></svg></div>
    <h3>It's Simple</h3>
    <p>Lorem ipsum dolor sit amet, consectetur adipiscing elit, sed do eiusmod tempor incididunt.</p>
  </div>
</section>

<section class="courses">
  <h2 class="section-title">LATEST <span>COURSES</span></h2>
  <div class="carousel-arrows"><i></i><i></i></div>
  <div class="course-grid">
    <article class="course-card">
      <div class="course-thumb" role="img" aria-label="Course cover artwork for Quick Fennish Fundamentals Suite" style="background:var(--yellow)"></div>
      <h4>QUICK FENNISH FUNDAMENTALS SUITE</h4>
      <div class="course-meta"><span class="stars">★★★★★</span><span>( 5 REVIEWS )</span></div>
      <div class="course-meta"><span>25 LESSONS</span><span class="price">$199</span></div>
      <div class="course-tutor"><span class="avatar"></span><div><b>Harold Wen Pike</b><small>Language Expert, Trainer</small></div></div>
    </article>
    <article class="course-card">
      <div class="course-thumb" role="img" aria-label="Course cover artwork for Quick Fennish and Fennish Nibbles bundle" style="background:linear-gradient(90deg,#f5c518 50%,#4fb3d9 50%)"></div>
      <h4>QUICK FENNISH + FENNISH NIBBLES BUNDLE</h4>
      <div class="course-meta"><span class="stars">★★★★★</span><span>( 5 REVIEWS )</span></div>
      <div class="course-meta"><span>40 LESSONS</span><span class="price">$159</span></div>
      <div class="course-tutor"><span class="avatar"></span><div><b>Harold Wen Pike</b><small>Language Expert, Trainer</small></div></div>
    </article>
    <article class="course-card">
      <div class="course-thumb" role="img" aria-label="Course cover artwork for Fennish Nibbles" style="background:#f2b705"></div>
      <h4>FENNISH NIBBLES</h4>
      <div class="course-meta"><span class="stars">★★★★★</span><span>( 4 REVIEWS )</span></div>
      <div class="course-meta"><span>15 LESSONS</span><span class="price">$15.99</span></div>
      <div class="course-tutor"><span class="avatar"></span><div><b>Harold Wen Pike</b><small>Language Expert, Trainer</small></div></div>
    </article>
    <article class="course-card">
      <div class="course-thumb" role="img" aria-label="Course cover artwork for Quick Fennish Fundamentals Suite bundle" style="background:linear-gradient(90deg,#f5c518 50%,#4fb3d9 50%)"></div>
      <h4>QUICK FENNISH FUNDAMENTALS SUITE</h4>
      <div class="course-meta"><span class="stars">★★★★★</span><span>( 5 REVIEWS )</span></div>
      <div class="course-meta"><span>25 LESSONS</span><span class="price">$199</span></div>
      <div class="course-tutor"><span class="avatar"></span><div><b>Harold Wen Pike</b><small>Language Expert, Trainer</small></div></div>
    </article>
  </div>
  <a class="more-btn" href="#">VIEW MORE COURSES</a>
</section>

<section class="info-band">
  <div class="band-col">
    <h3><span>NEWS</span> / Up-Coming Courses</h3>
    <div class="news-list">
      <div class="news-item"><i></i><div><b>QUICK FENNISH FUNDAMENTALS SUITE</b><small>15 March 2015</small></div></div>
      <div class="news-item"><i></i><div><b>QUICK FENNISH FUNDAMENTALS SUITE</b><small>15 March 2015</small></div></div>
      <div class="news-item"><i></i><div><b>QUICK FENNISH FUNDAMENTALS SUITE</b><small>15 March 2015</small></div></div>
      <div class="news-item"><i></i><div><b>QUICK FENNISH FUNDAMENTALS SUITE</b><small>15 March 2015</small></div></div>
    </div>
  </div>
  <div class="band-col join-form">
    <h3><span>Your</span> Journey Start Here!</h3>
    <div class="field">Name</div>
    <div class="field">Email</div>
    <div class="field">Phone</div>
    <div class="field tall">Your Message</div>
    <a class="join-btn" href="#">Join!</a>
    <p>*Academy for Organisations and Academic Institutes Coming Soon!</p>
  </div>
  <div class="band-col">
    <h3><span>Featured</span> Instructor</h3>
    <div class="tutor-card">
      <div class="tutor-photo" role="img" aria-label="Portrait photo of the featured instructor"></div>
      <h4>Harold Wen Pike</h4>
      <div class="role">Language Expert, Trainer</div>
      <p>Lorem ipsum dolor sit amet, consectetur adipiscing elit, sed do eiusmod tempor incididunt ut labore.</p>
      <a class="profile-btn" href="#">VIEW PROFILE</a>
    </div>
  </div>
</section>

<section class="testimonials">
  <h2 class="section-title">WHAT <span>STUDENT</span> SAY ?</h2>
  <blockquote>“LOREM IPSUM DOLOR SIT AMET, CONSECTETUR ADIPISCING ELIT, SED DO EIUSMOD TEMPOR INCIDIDUNT UT LABORE ET DOLORE MAGNA ALIQUA.”</blockquote>
  <div class="student-photo" role="img" aria-label="Portrait photo of a student"></div>
  <div class="student-name">ANNA RYLAND</div>
  <div class="dots"><i class="on"></i><i></i><i></i></div>
</section>

<footer class="site-footer">
  <div class="social">
    <div class="social-box"><i></i><div><b>Chirpline</b><small>14,125</small></div></div>
    <div class="social-box"><i></i><div><b>Friendwall</b><small>10,219</small></div></div>
    <div class="social-box"><i></i><div><b>Circleplus</b><small>18,416</small></div></div>
  </div>
  <nav class="footer-nav">
    <a href="#">About Us</a><a href="#">Affiliates</a><a href="#">Blog</a><a href="#">Support</a><a href="#">Contact Us</a><a href="#">Careers</a><a href="#">Terms of Use</a><a href="#">Privacy Policy</a>
  </nav>
  <div class="copyright">Copyright © 2015 brivora-learn.test. All Rights Reserved</div>
</footer>

</body>
</html>
```